ASSET BASED PROGRAM FLIER

Need flier to market hard money loan products offered HARD MONEY FIX & FLIP PROGRAMS

We offer a variety of loan programs Some program highlights include......

1) No Minimum Credit Score
2) 3-5 Day Close
3) Up to 100% of Purchase & Rehab
4) Rates as Low as 7%
5) Loans Offered Nationwide

Contact us today for more information at (800) 416-2905 x42 or email us at mvoss@brightlanelending.com NMLS #781536 www.brightlanelending.com

```html
<!DOCTYPE html>
<html lang="en">
<head>
<meta charset="utf-8">
<title>Hard Money Fix &amp; Flip Programs – Brightlane Lending</title>
<link rel="stylesheet" href="https://fonts.googleapis.com/css2?family=Montserrat:wght@600&family=Quicksand:wght@400;500&family=Lato:wght@400;700&display=swap">
<style>
  :root {
    --navy: #154c86;
    --navy-deep: #0f3c70;
    --navy-light: #2a679f;
    --white: #ffffff;
    --paper: #f4f5f6;
    --ink: #3d3f42;
    --gold: #a88f3c;
    --title-box: rgba(90, 90, 92, 0.72);
  }
  * { margin: 0; padding: 0; box-sizing: border-box; }
  html, body { width: 922px; height: 1200px; overflow: hidden; background: var(--white); }
  .flier { position: relative; width: 922px; height: 1200px; background: var(--white); }

  .header {
    position: absolute; left: 0; top: 0; width: 922px; height: 140px;
    background: linear-gradient(180deg, #ffffff 0%, #f3f4f5 100%);
  }
  .brand {
    position: absolute; left: 44px; top: 52px;
    display: flex; align-items: center; gap: 10px;
    font-family: "Montserrat", sans-serif; font-weight: 600; font-size: 19px;
    color: var(--navy);
  }
  .brand-dot { width: 26px; height: 26px; border-radius: 50%; background: var(--gold); }
  .website {
    position: absolute; right: 42px; top: 60px;
    font-family: "Quicksand", sans-serif; font-weight: 500; font-size: 18px;
    letter-spacing: 1px; color: #2c2d30;
  }
  .website-rule {
    position: absolute; right: 48px; top: 87px; width: 78px; height: 2px; background: #9a9ca0;
  }

  .hero {
    position: absolute; left: 0; top: 140px; width: 922px; height: 546px;
    background:
      radial-gradient(ellipse at 60% 65%, #f4f2ef 0%, rgba(244,242,239,0) 55%),
      linear-gradient(160deg, #e9dcc5 0%, #d9d6d2 35%, #b8b1aa 60%, #e7e6e4 85%, #f3f3f3 100%);
  }
  .hero-title {
    position: absolute; left: 196px; top: 346px; width: 532px; height: 140px;
    background: var(--title-box);
    display: flex; align-items: center; justify-content: center; text-align: center;
    font-family: "Montserrat", sans-serif; font-weight: 600; font-size: 45px; line-height: 46px;
    color: var(--white); letter-spacing: 0.5px;
  }

  .highlights {
    position: absolute; left: 0; top: 686px; width: 922px; height: 618px;
    background: radial-gradient(ellipse at 50% 35%, var(--navy-light) 0%, var(--navy) 45%, var(--navy-deep) 100%);
  }
  .highlights-band { position: absolute; left: 0; top: 686px; width: 922px; height: 618px; }
  .highlight-list {
    position: absolute; left: 0; top: 728px; width: 922px; list-style: none; text-align: center;
    font-family: "Quicksand", sans-serif; font-weight: 500; font-size: 24px; color: var(--white);
  }
  .highlight-list li { height: 42.5px; line-height: 42.5px; position: relative; }
  .highlight-list li + li::before {
    content: ""; position: absolute; left: 50%; top: 0; width: 170px; margin-left: -85px;
    height: 1px; background: rgba(255,255,255,0.25);
  }

  .footer {
    position: absolute; left: 0; top: 1039px; width: 922px; height: 161px;
    background: linear-gradient(180deg, #ffffff 0%, #eef0f1 100%);
  }
  .gallery { position: absolute; top: 985px; height: 137px; width: 211px; }
  .gallery--meeting { left: 125px; background: linear-gradient(135deg, #e8e4dc 0%, #a89b86 50%, #3c3d44 100%); }
  .gallery--carpentry { left: 356px; background: linear-gradient(135deg, #6a5a48 0%, #3e5f86 55%, #2b2622 100%); }
  .gallery--builder { left: 586px; background: linear-gradient(135deg, #e9eaea 0%, #c7a56a 45%, #8e3b36 100%); }
  .nmls {
    position: absolute; right: 26px; top: 1021px;
    font-family: "Lato", sans-serif; font-size: 11px; color: var(--white);
  }
  .contact {
    position: absolute; left: 0; top: 1140px; width: 922px; text-align: center;
    font-family: "Lato", sans-serif; font-size: 17px; line-height: 23px; color: var(--ink);
  }
  .contact strong { font-weight: 700; }
</style>
</head>
<body>
<main class="flier">
  <header class="header">
    <div class="brand"><span class="brand-dot"></span>Brightlane Lending</div>
    <div class="website">www.brightlanelending.com</div>
    <div class="website-rule"></div>
  </header>

  <section class="hero" role="img" aria-label="Close-up of a person in a white shirt signing loan documents with a pen at a bright desk"></section>
  <h1 class="hero-title">HARD MONEY FIX &amp;<br>FLIP PROGRAMS</h1>

  <section class="highlights"></section>
  <ul class="highlight-list">
    <li>No Minimum Credit Score</li>
    <li>3-5 Day Close</li>
    <li>Up to 100% of Purchase &amp; Rehab</li>
    <li>Rates as Low as 7%</li>
    <li>Loans Offered Nationwide</li>
  </ul>
  <div class="nmls">NMLS #781536</div>

  <footer class="footer"></footer>
  <div class="gallery gallery--meeting" role="img" aria-label="Businesspeople in hard hats reviewing plans in a renovated kitchen"></div>
  <div class="gallery gallery--carpentry" role="img" aria-label="Worker in a hard hat using a power tool on wooden boards"></div>
  <div class="gallery gallery--builder" role="img" aria-label="Smiling builder in a hard hat carrying lumber on a job site"></div>
  <p class="contact">Contact us today for more information at <strong>(800) 416-2905 x42</strong><br>or email us at <strong>mvoss@brightlanelending.com</strong></p>
</main>
</body>
</html>
```